Business Card for Fashion House

We need a business card design for our personalize fashion service for our customers. the business card should reflect reliability, luxury and creativity.
The brand Vastrelle is extracted from "Vibrant Estrella"; Vastrelle provides fashion designs sprinkled with luxury and style tailored for our elite clients character profile.
Vastrelle is created for those who embody class and elegance with a passion for style.
Target Market(s)
Affluent Customers
Industry/Entity Type
Fashion
Contact Information for Business Card
Noura Al Hashimi
Fashion Designer
Telephone: +971 5550192
Mobile +971 555073
Emal q@k.example
Website www.vastrelle.example
Social Media Youtube g+ Facebook Instagram Pin /vastrelle
Font styles to use
Other font styles liked:
- Audrey provided
Look and feel
Each slider illustrates characteristics of the customer's brand and the style your logo design should communicate.

```html
<!DOCTYPE html>
<html lang="en">
<head>
<meta charset="utf-8">
<title>Vastrelle Business Card</title>
<link rel="stylesheet" href="https://fonts.googleapis.com/css2?family=Cinzel:wght@400&family=Marcellus&family=EB+Garamond:wght@400;500&display=swap">
<style>
  :root {
    --stage: #d9d6d3;
    --espresso: #3b3331;
    --espresso-deep: #322b29;
    --paper: #f4f3f1;
    --paper-shade: #e6e4e1;
    --ink: #3a3432;
    --ink-soft: #6e6866;
    --muted-light: #8e8784;
    --white: #ffffff;
  }
  * { margin: 0; padding: 0; box-sizing: border-box; }
  html, body { width: 1200px; height: 1000px; overflow: hidden; }
  body {
    background: var(--stage);
    position: relative;
    font-family: "EB Garamond", Georgia, serif;
  }
  .card {
    position: absolute;
    left: 250px;
    width: 700px;
    height: 400px;
    border-radius: 26px;
    overflow: hidden;
    box-shadow: 0 10px 28px rgba(0,0,0,0.18);
  }

  /* Back side */
  .card--back {
    top: 60px;
    background: linear-gradient(160deg, var(--espresso) 0%, var(--espresso-deep) 100%);
    color: var(--white);
    text-align: center;
  }
  .card--back .brand-dot {
    position: absolute;
    left: 326px; top: 78px;
    width: 48px; height: 48px;
    border-radius: 50%;
    border: 2px solid var(--white);
  }
  .card--back .wordmark {
    position: absolute;
    left: 0; right: 0; top: 170px;
    font-family: "Cinzel", Georgia, serif;
    font-size: 54px;
    letter-spacing: 0.42em;
    padding-left: 0.42em;
    color: var(--white);
  }
  .card--back .site {
    position: absolute;
    left: 0; right: 0; top: 278px;
    font-family: "EB Garamond", Georgia, serif;
    font-size: 20px;
    letter-spacing: 0.04em;
    color: var(--muted-light);
  }
  .card--back .site strong { color: var(--white); font-weight: 500; }

  /* Front side */
  .card--front {
    top: 540px;
    background: linear-gradient(180deg, var(--paper) 0%, var(--paper-shade) 100%);
    color: var(--ink);
  }
  .card--front .brand-dot {
    position: absolute;
    left: 326px; top: 38px;
    width: 48px; height: 48px;
    border-radius: 50%;
    border: 2px solid var(--ink);
  }
  .card--front .wordmark {
    position: absolute;
    left: 30px; width: 360px; top: 174px;
    text-align: center;
    font-family: "Cinzel", Georgia, serif;
    font-size: 30px;
    letter-spacing: 0.36em;
    color: var(--ink);
  }
  .band {
    position: absolute;
    left: 0; right: 0; top: 246px;
    height: 102px;
    background: var(--espresso);
  }
  .divider {
    position: absolute;
    left: 412px; top: 112px;
    width: 1px; height: 170px;
    background: var(--muted-light);
  }
  .contact-list {
    position: absolute;
    left: 432px; top: 112px;
    list-style: none;
    font-size: 17px;
    line-height: 30px;
    letter-spacing: 0.04em;
    color: var(--ink-soft);
  }
  .contact-list li { display: flex; align-items: center; gap: 10px; }
  .contact-list svg { width: 15px; height: 15px; fill: var(--ink); flex: none; }
  .holder {
    position: absolute;
    left: 52px; top: 266px;
    color: var(--white);
    text-align: right;
  }
  .holder .name {
    font-family: "Marcellus", Georgia, serif;
    font-size: 30px;
    letter-spacing: 0.02em;
  }
  .holder .role {
    font-size: 18px;
    color: var(--paper-shade);
    margin-top: -4px;
  }
  .social {
    position: absolute;
    left: 440px; top: 300px;
    display: flex; align-items: center; gap: 10px;
  }
  .social .dot {
    width: 22px; height: 22px;
    border-radius: 50%;
    background: var(--paper);
  }
  .social .handle {
    margin-left: 6px;
    font-size: 19px;
    color: var(--white);
    letter-spacing: 0.03em;
  }
</style>
</head>
<body>

<section class="card card--back" aria-label="Card back">
  <div class="brand-dot"></div>
  <div class="wordmark">VASTRELLE</div>
  <div class="site">www.<strong>vastrelle</strong>.example</div>
</section>

<section class="card card--front" aria-label="Card front">
  <div class="brand-dot"></div>
  <div class="wordmark">VASTRELLE</div>
  <div class="band"></div>
  <div class="divider"></div>

  <ul class="contact-list">
    <li>
      <svg viewBox="0 0 16 16" aria-hidden="true"><rect x="1" y="5" width="14" height="9" rx="2"/><rect x="3" y="2" width="10" height="4" rx="2"/></svg>
      +971 5550192
    </li>
    <li>
      <svg viewBox="0 0 16 16" aria-hidden="true"><path d="M3 1l3 3-2 2c1 2 3 4 6 6l2-2 3 3-2 2C7 15 1 9 1 3z"/></svg>
      +971 555073
    </li>
    <li>
      <svg viewBox="0 0 16 16" aria-hidden="true"><circle cx="8" cy="8" r="7"/></svg>
      www.vastrelle.example
    </li>
    <li>
      <svg viewBox="0 0 16 16" aria-hidden="true"><rect x="1" y="3" width="14" height="10" rx="2"/></svg>
      q@k.example
    </li>
  </ul>

  <div class="holder">
    <div class="name">NOURA AL HASHIMI</div>
    <div class="role">Fashion Designer</div>
  </div>

  <div class="social" aria-label="Social profiles">
    <span class="dot"></span>
    <span class="dot"></span>
    <span class="dot"></span>
    <span class="dot"></span>
    <span class="dot"></span>
    <span class="handle">/vastrelle</span>
  </div>
</section>

</body>
</html>
```